Business Card Design

I need a business card design for a new business based in South West Australia.
I specialize in residential window cleaning & general handyman maintenance.

Industry/Entity Type

Business

Contact Information for Business Card

Dale Marsh - 512 SILVER HAWK DETAILING
- Window Cleaning
- House Maintenance

```html
<!DOCTYPE html>
<html lang="en">
<head>
<meta charset="utf-8">
<title>512 Silver Hawk Detailing – Business Card</title>
<link href="https://fonts.googleapis.com/css2?family=Open+Sans:wght@400;600;700&display=swap" rel="stylesheet">
<style>
  :root {
    --bg: #e9e6e1;
    --card: #ffffff;
    --brand-blue: #0d4f9c;
    --name-blue: #1a4f8f;
    --text-grey: #4a4a4a;
    --pattern-light: #e3ebf6;
    --pattern-mid: #c4d4ea;
    --shadow: rgba(0,0,0,0.18);
  }
  * { margin: 0; padding: 0; box-sizing: border-box; }
  html, body { width: 1200px; height: 900px; overflow: hidden; }
  body {
    background: var(--bg);
    font-family: "Open Sans", sans-serif;
    position: relative;
  }
  .card {
    position: absolute;
    width: 600px;
    height: 343px;
    background: var(--card);
    box-shadow: 0 6px 18px var(--shadow);
    overflow: hidden;
  }
  .card-back { left: 90px; top: 120px; }
  .card-front { left: 510px; top: 430px; }

  .window-pattern {
    position: absolute;
    inset: 0;
    background: linear-gradient(135deg, var(--pattern-light) 0%, var(--pattern-mid) 100%);
  }

  .business-name {
    font-weight: 700;
    color: var(--brand-blue);
    font-size: 26px;
    line-height: 1.1;
    white-space: nowrap;
  }
  .services {
    font-weight: 400;
    color: var(--text-grey);
    font-size: 13px;
    margin-top: 6px;
    white-space: nowrap;
  }

  .back-brand {
    position: absolute;
    right: 22px;
    top: 200px;
    background: var(--card);
    padding: 10px 14px 10px;
  }
  .back-brand .business-name { font-size: 24px; }

  .person {
    position: absolute;
    left: 340px;
    top: 22px;
  }
  .person-name {
    color: var(--name-blue);
    font-size: 21px;
    font-weight: 600;
    line-height: 1.1;
  }
  .person-title {
    color: var(--text-grey);
    font-size: 13px;
    margin-left: 8px;
  }
  .contact-list {
    list-style: none;
    position: absolute;
    left: 368px;
    top: 84px;
  }
  .contact-list li {
    display: flex;
    align-items: center;
    gap: 8px;
    color: var(--text-grey);
    font-size: 14px;
    line-height: 22px;
  }
  .contact-list svg { width: 12px; height: 12px; fill: var(--brand-blue); }

  .front-brand {
    position: absolute;
    left: 50px;
    top: 250px;
  }
  .name-row {
    display: flex;
    align-items: center;
    gap: 12px;
  }
  .brand-dot {
    width: 30px;
    height: 30px;
    border-radius: 50%;
    background: var(--brand-blue);
    flex: none;
  }
  .front-brand .services { margin-left: 42px; }
</style>
</head>
<body>

<section class="card card-back">
  <div class="window-pattern" role="img" aria-label="Repeating pattern of pale blue arched window motifs"></div>
  <div class="back-brand">
    <div class="business-name">512 Silver Hawk Detailing</div>
    <div class="services">Window Cleaning · House Maintenance</div>
  </div>
</section>

<section class="card card-front">
  <div class="person">
    <div class="person-name">Dale Marsh</div>
    <div class="person-title">Managing Director</div>
  </div>
  <ul class="contact-list">
    <li><svg viewBox="0 0 24 24"><path d="M6.6 10.8a15 15 0 0 0 6.6 6.6l2.2-2.2a1 1 0 0 1 1-.25 11.4 11.4 0 0 0 3.6.57 1 1 0 0 1 1 1V20a1 1 0 0 1-1 1A17 17 0 0 1 3 4a1 1 0 0 1 1-1h3.5a1 1 0 0 1 1 1c0 1.25.2 2.450.57 3.57a1 1 0 0 1-.25 1z"/></svg>044-512-0318</li>
    <li><svg viewBox="0 0 24 24"><path d="M6 2h10v6H6zM4 9h16a2 2 0 0 1 2 2v9H2v-9a2 2 0 0 1 2-2zm3 4v2h4v-2zm0 3v2h4v-2zm7-3v5h4v-5z"/></svg>123-512-0319</li>
    <li><svg viewBox="0 0 24 24"><path d="M7 1h10a2 2 0 0 1 2 2v18a2 2 0 0 1-2 2H7a2 2 0 0 1-2-2V3a2 2 0 0 1 2-2zm0 3v14h10V4zm5 15.5a1.2 1.2 0 1 0 0 2.4 1.2 1.2 0 0 0 0-2.4z"/></svg>123-512-0320</li>
    <li><svg viewBox="0 0 24 24"><path d="M2 5h20v14H2zm2 2v.5l8 5 8-5V7l-8 5z"/></svg>info@silverhawk.com</li>
    <li><svg viewBox="0 0 24 24"><path d="M10.6 13.4a1 1 0 0 0 1.4 0l4-4a1 1 0 1 0-1.4-1.4l-4 4a1 1 0 0 0 0 1.4zM8.5 20.5a4 4 0 0 1-2.8-6.8l2.4-2.4 1.4 1.4-2.4 2.4a2 2 0 0 0 2.8 2.8l2.4-2.4 1.4 1.4-2.4 2.4a4 4 0 0 1-2.8 1.2zm7.4-7.8-1.4-1.4 2.4-2.4a2 2 0 0 0-2.8-2.8l-2.4 2.4-1.4-1.4 2.4-2.4a4 4 0 0 1 5.6 5.6z"/></svg>www.silverhawk.com</li>
  </ul>
  <div class="front-brand">
    <div class="name-row">
      <span class="brand-dot"></span>
      <span class="business-name">512 Silver Hawk Detailing</span>
    </div>
    <div class="services">Window Cleaning · House Maintenance</div>
  </div>
</section>

</body>
</html>
```